Refresh www.pollbrightclass.com.au & design new logo

We need a new refreshed website for our site www.pollbrightclass.com.au

We provide an survey service for schools, providing feedback from teachers, students and parents. The survey functionality is done through query otter, so the refresh is simply for the website, which needs to sell the service to our target market which is mainly principals of school.

We want a new fresh look, so are looking for a logo redesign as well. We are flexible with colours as well (does not need to be the same blue as is used at the moment.

Re the website, We are happy to look at Navigation and page changes. Also need to include a call to action- perhaps a "sign up now" or email for more information on the home page. I have used a wordpress site before, but an not an expert. Items I would like to edit in the future is pricing, changing the sample reports to be sent out etc.

Target Market(s)

Principals and teachers of schools who are seeking formative feedback from their parents, students and teachers

Industry/Entity Type

School

Font styles to use
Serif
Sans Serif

Colors

Designer to choose colors to be used in the design.

Requirements
Must have
• Call to action on home page- inviting to email for more information
Link to video explaining the surveys
Ability to download sample reports
home/sample reports/parents/teachers/parents/testimonials/about us/benefits/pricing

```html
<!DOCTYPE html>
<html lang="en">
<head>
<meta charset="utf-8">
<title>Poll Bright Class</title>
<link href="https://fonts.googleapis.com/css2?family=Oswald:wght@400;500&family=Open+Sans:wght@400;600&display=swap" rel="stylesheet">
<style>
:root{
  --sky-top:#7fc0ee;
  --sky-bottom:#d9ecfa;
  --green:#6ea52a;
  --green-bright:#7cbf2f;
  --plum:#9b0f5a;
  --cyan:#1fb1d8;
  --ink:#2b2b2b;
  --body:#555;
  --red:#e0403f;
  --blue:#1a8ad8;
  --heading-blue:#3d6e9a;
}
*{box-sizing:border-box;margin:0;padding:0}
html,body{width:786px;height:1200px;overflow:hidden}
body{
  position:relative;
  font-family:"Open Sans",sans-serif;
  color:var(--body);
  background:linear-gradient(180deg,var(--sky-top) 0%,#a9d4f4 40%,var(--sky-bottom) 70%,#c8e2f7 100%);
}
.abs{position:absolute}
.brand{
  background:#fff;display:flex;align-items:center;justify-content:center;gap:6px;
  font-family:"Oswald",sans-serif;font-weight:500;color:var(--ink);letter-spacing:.2px;white-space:nowrap;
}
.brand .dot{width:7px;height:7px;background:var(--green);border-radius:50%}
.brand-top{left:112px;top:30px;width:140px;height:38px;font-size:15px}
.phone{right:116px;top:42px;font-family:"Oswald",sans-serif;color:#fff;font-size:16px;white-space:nowrap}
.nav{left:110px;top:79px;width:564px;height:39px;background:var(--green-bright);display:flex;justify-content:space-between;padding-right:10px}
.nav a{
  font-family:"Oswald",sans-serif;font-size:10px;color:#fff;text-decoration:none;white-space:nowrap;
  display:flex;align-items:center;padding:0 2px;text-transform:uppercase;letter-spacing:-.1px;
}
.nav a.active{background:#1d1d1d;padding:0 12px}
.hero{
  left:113px;top:118px;width:561px;height:300px;
  background:linear-gradient(120deg,#c9a98a 0%,#e9c7a3 30%,#b7cbe0 60%,#6c9fd0 100%);
  box-shadow:0 12px 14px -8px rgba(0,0,0,.35);
}
.hero-dots{right:20px;top:18px;display:flex;flex-direction:column;gap:4px}
.hero-dots i{width:7px;height:7px;border-radius:50%;background:#111}
.hero-dots i:first-child{background:#fff}
.caption{left:0;top:192px;width:320px;height:72px;background:rgba(80,80,80,.45);padding:13px 0 0 28px}
.caption h1{font-family:"Oswald",sans-serif;font-weight:500;color:#fff;font-size:21px;line-height:1.1;white-space:nowrap;letter-spacing:-.3px}
.caption p{font-family:"Oswald",sans-serif;color:#fff;font-size:12px;margin-top:6px;white-space:nowrap}
.card{
  top:448px;width:178px;height:212px;border-radius:28px 28px 0 0;text-align:center;color:#fff;
  box-shadow:0 10px 10px -6px rgba(0,0,0,.3);
}
.card h2{font-family:"Oswald",sans-serif;font-weight:400;font-size:17px;margin-top:20px}
.card .photo{width:156px;height:88px;margin:8px auto 0;border-radius:2px}
.card p{font-size:8px;line-height:1.65;margin:7px 8px 0}
.card .more{display:inline-block;background:#fff;color:#222;font-size:7.5px;padding:4px 10px;border-radius:9px;margin-top:10px;font-weight:600}
.student{left:112px;background:var(--green)}
.student .photo{background:linear-gradient(135deg,#f2c33a,#e9508e,#3aa0e0)}
.parent{left:304px;background:var(--plum)}
.parent .photo{background:linear-gradient(135deg,#eee,#d8c6b6,#f5f5f5)}
.staff{left:497px;background:var(--cyan)}
.staff .photo{background:linear-gradient(135deg,#8e8c84,#c9b9a4,#6f7b84)}
.provide{left:113px;top:692px;width:258px}
.provide h3{font-family:"Oswald",sans-serif;font-weight:400;color:var(--ink);font-size:13.5px}
.provide h3 span{color:var(--green)}
.provide p{font-size:7.6px;line-height:1.7;margin-top:9px;text-align:justify}
.provide ul{list-style:none;margin-top:12px}
.provide li{font-size:8.6px;color:#333;margin-bottom:14px;display:flex;align-items:center;gap:7px}
.provide li svg{flex:none}
.video{left:392px;top:686px;width:284px;height:173px;background:#fff;border:1px solid #ccc;padding:7px}
.video .screen{width:100%;height:100%;background:linear-gradient(135deg,#8a6a48,#c7a07a,#7a5d44);position:relative}
.video .bar{position:absolute;left:0;right:0;bottom:0;height:20px;background:#1b1b1b;display:flex;align-items:center;padding:0 8px;gap:8px;font-size:6px;color:#ddd}
.video .track{flex:1;height:2px;background:#555;position:relative}
.video .track i{position:absolute;left:0;top:0;width:35%;height:2px;background:#d8342f}
.video .play{position:absolute;left:50%;top:45%;transform:translate(-50%,-50%)}
.box{top:880px;height:121px;background:linear-gradient(180deg,#fff,#f0f0f0);box-shadow:0 2px 6px rgba(0,0,0,.2)}
.download{left:112px;width:344px;padding:18px 16px}
.download h3{font-family:"Open Sans",sans-serif;font-weight:400;font-size:12.5px;color:#222}
.download h3 span{color:var(--green)}
.download p{font-size:6.6px;line-height:1.8;margin-top:8px}
.download .btns{display:flex;gap:9px;margin-top:13px}
.download .btns span{background:var(--green-bright);color:#fff;font-size:7.8px;padding:7px 7px;border-bottom:2px solid #5a8f1f;white-space:nowrap}
.newsletter{left:468px;width:206px;border-top:4px solid var(--blue);text-align:center;padding-top:18px}
.newsletter h3{font-weight:400;color:var(--red);font-size:11px}
.newsletter p{font-size:7.6px;color:#333;margin-top:4px}
.newsletter .field{width:148px;height:21px;margin:9px auto 0;border:1px solid #aaa;background:#fff;font-size:6.5px;text-align:left;padding:5px 4px;color:#555}
.newsletter .sub{display:inline-block;margin-top:9px;background:var(--blue);color:#fff;font-size:6.5px;font-weight:600;padding:5px 13px;border-radius:3px}
.foot-col{top:1036px}
.foot-col h4{font-weight:400;color:var(--heading-blue);font-size:9.5px;padding-bottom:6px;border-bottom:1px solid #b9c7d2}
.foot-col p{font-size:7px;line-height:1.75;color:#444}
.contact{left:113px;width:130px}
.contact p{margin-top:6px;white-space:nowrap}
.social{left:300px;width:190px}
.social .item{display:flex;gap:8px;margin-top:8px}
.social .thumb{width:41px;height:32px;background:linear-gradient(135deg,#4f6f8e,#c9b68f);flex:none}
.social .item b{font-weight:400;color:var(--green);font-size:8px;display:block}
.social .item p{font-size:6.4px;line-height:1.6}
.partners{left:534px;width:141px}
.partners .badges{display:flex;gap:10px;margin-top:10px;align-items:center}
.partners .badges i{display:block;height:24px}
.rule{left:112px;top:1130px;width:570px;height:1px;background:#c3d5e3}
.brand-foot{left:113px;top:1144px;width:107px;height:30px;font-size:11.5px}
.icons{left:344px;top:1148px;display:flex;gap:5px}
.icons i{width:20px;height:20px;border-radius:2px;display:block}
.copy{right:119px;top:1156px;font-size:8.6px;color:#333;white-space:nowrap}
</style>
</head>
<body>
  <div class="abs brand brand-top">Poll Bright Class<span class="dot"></span></div>
  <div class="abs phone">Phone (555) 2049318</div>

  <nav class="abs nav">
    <a class="active">Home</a><a>Sample Reports</a><a>Parents</a><a>Teachers</a><a>Parents</a><a>Testimonials</a><a>About Us</a><a>Benefits</a><a>Pricing</a>
  </nav>

  <section class="abs hero" role="img" aria-label="Smiling school children at a classroom desk with coloured pencils">
    <div class="abs hero-dots"><i></i><i></i><i></i><i></i></div>
    <div class="abs caption">
      <h1>SURVEY SERVICE FOR SCHOOLS</h1>
      <p>Lorem Ipsum is simply dummy text of the printing</p>
    </div>
  </section>

  <article class="abs card student">
    <h2>Student Surveys</h2>
    <div class="photo" role="img" aria-label="Group of students in colourful shirts forming a circle"></div>
    <p>Lorem ipsum dolor sit amet, consectetur adipiscing elit, sed do eiusmod tempor</p>
    <span class="more">Read More</span>
  </article>
  <article class="abs card parent">
    <h2>Parent Surveys</h2>
    <div class="photo" role="img" aria-label="Parents cheering beside their child at a desk"></div>
    <p>Lorem ipsum dolor sit amet, consectetur adipiscing elit, sed do eiusmod tempor</p>
    <span class="more">Read More</span>
  </article>
  <article class="abs card staff">
    <h2>Staff Surveys</h2>
    <div class="photo" role="img" aria-label="School staff group giving thumbs up"></div>
    <p>Lorem ipsum dolor sit amet, consectetur adipiscing elit, sed do eiusmod tempor</p>
    <span class="more">Read More</span>
  </article>

  <section class="abs provide">
    <h3>WE PROVIDE AN <span>SURVEY SERVICE</span></h3>
    <p>A HAPPY school staff is a more effective staff and one of the key factors is the effectiveness of the school's leadership. School staff opinion surveys ONLY provide data and do not provide any real,</p>
    <ul>
      <li><svg width="6" height="6" viewBox="0 0 6 6"><path d="M0 0l3 3-3 3M3 0l3 3-3 3" fill="none" stroke="#6ea52a" stroke-width="1"/></svg>Service for schools</li>
      <li><svg width="6" height="6" viewBox="0 0 6 6"><path d="M0 0l3 3-3 3M3 0l3 3-3 3" fill="none" stroke="#6ea52a" stroke-width="1"/></svg>Providing feedback from teachers</li>
      <li><svg width="6" height="6" viewBox="0 0 6 6"><path d="M0 0l3 3-3 3M3 0l3 3-3 3" fill="none" stroke="#6ea52a" stroke-width="1"/></svg>Students and parents</li>
    </ul>
  </section>

  <div class="abs video">
    <div class="screen" role="img" aria-label="Video still of smiling students in a classroom">
      <svg class="play" width="34" height="34" viewBox="0 0 34 34"><circle cx="17" cy="17" r="16" fill="rgba(0,0,0,.45)"/><path d="M13 10l11 7-11 7z" fill="#fff"/></svg>
      <div class="bar">
        <svg width="9" height="9" viewBox="0 0 9 9"><circle cx="4.5" cy="4.5" r="4" fill="none" stroke="#fff"/><path d="M3.5 2.8l2.5 1.7-2.5 1.7z" fill="#fff"/></svg>
        <svg width="22" height="7" viewBox="0 0 22 7"><path d="M0 2h2l2-2v7l-2-2H0z" fill="#d8342f"/><path d="M8 1v5M10 1v5M12 1v5M14 1v5M16 1v5" stroke="#d8342f"/></svg>
        <div class="track"><i></i></div>
        <span>01:30 / 04:55</span>
        <svg width="8" height="6" viewBox="0 0 8 6"><rect x=".5" y=".5" width="7" height="5" fill="none" stroke="#fff"/></svg>
        <svg width="7" height="7" viewBox="0 0 7 7"><circle cx="3.5" cy="3.5" r="2.5" fill="none" stroke="#fff" stroke-width="1.5"/></svg>
      </div>
    </div>
  </div>

  <section class="abs box download">
    <h3>DOWNLOAD <span>SAMPLE REPORTS</span></h3>
    <p>Lorem Ipsum has been the industry's standard dummy text ever since the 1500s, when an unknown printer took a galley of type and scrambled it to make a type specimen book. It has survived</p>
    <div class="btns"><span>Sample Staff Surveys</span><span>Sample Parent Surveys</span><span>Sample Student Surveys</span></div>
  </section>

  <section class="abs box newsletter">
    <h3>NEWSLETTERS SIGNUP</h3>
    <p>Sign Up for Our Newsletter:</p>
    <div class="field">Email</div>
    <span class="sub">SUBSCRIBE</span>
  </section>

  <section class="abs foot-col contact">
    <h4>CONTACT</h4>
    <p>14 Wattle Lane BROOKDALE QLD 4012<br>Email: info@pollbrightclass.com.au<br>Phone 0400 318 527</p>
  </section>
  <section class="abs foot-col social">
    <h4>SOCIAL</h4>
    <div class="item">
      <div class="thumb" role="img" aria-label="Thumbnail of a school event"></div>
      <div><b>Doing a great job!</b><p>07/04/2013<br>Sometimes it feels great to hear your doing</p></div>
    </div>
  </section>
  <section class="abs foot-col partners">
    <h4>PARTNERS</h4>
    <div class="badges">
      <i style="width:30px;height:27px;background:#1a8ad8"></i>
      <i style="width:38px;height:18px;background:#555;border-radius:3px"></i>
      <i style="width:50px;height:12px;background:#9a9a9a;border-radius:6px"></i>
    </div>
  </section>

  <div class="abs rule"></div>
  <div class="abs brand brand-foot">Poll Bright Class<span class="dot"></span></div>
  <div class="abs icons">
    <i style="background:#29a9e1"></i><i style="background:#d6342b"></i><i style="background:#3b5a9a"></i><i style="background:#1776b0"></i>
  </div>
  <div class="abs copy">Copyright © 2015 All Rights</div>
</body>
</html>
```